Design a sleek menu for our new smoothie and snacks shop”Blend”

requiring a store drinks and snacks menu we would like to have a white background for the menu . I would like to have fruit watermarks like in our original design concept , For reference ,please refer to the pictures . The font and layout of the menu should be modern , simple but stylish and reflect a smoothie shop.
we will be proving the menu contents to input once we agree to the design concept .
here are the menu documents

smoothies

Regular 16oz £4.99 Large 20oz £5.99
substitute semi skim for any dairy free milks for .50p
add vegan protein or regular protein for .50p

Jam jar jive
mixed berries, banana, coconut yogurt, milk

Leafy Rocket
Spinach, avocado, matcha, banana, milk, agave

Ride the violet wave
Blueberries, banana, açai, coconut milk

Peachy Cyclone
Mango, apple, strawberry, coconut milk, vanilla yogurt, agave

Hop Hare Blend
Oats, banana, cinnamon, dates, almond butter

Tropic Lagoon
Pineapple, spinach, banana, coconut milk

Bean scene
Oats, banana, cinnamon, cocoa, espresso, skim milk

Choco Plantain
Oats, banana, cocoa, cinnamon, peanut butter , agave
*almond butter substitute is available

Nut & Jam Joy
Frozen berries, banana, peanut butter, maple syrup, coconut milk
*Spinach is optional

Strawberry Blend
Strawberries, banana, coconut milk, orange juice, agave

Chard Charge
Spinach, kale, pineapple, apple juice

Fresh Spark
Celery, lemon, apple

Cherry Charming
Blueberries, banana, vanilla yogurt, soy milk, collagen protein, agave,

Shakes
Large 16oz £6
Add Protein for .50p

Nutty Whip
Avocado, banana, skim milk, vanilla

Choco Whirl
Avocado, cocoa powder, coconut milk, banana, maple syrup
*can substitute avocado with dairy free ice cream

Plant Treat
Dairy free vanilla Ice cream, banana, cocoa powder, coconut milk, agave

The final swirl
Strawberry ,dates , dairy free ice cream, coconut milk, agave
*substitute dairy free ice cream for avocado

Buzz rush
Espresso, banana, dairy free ice cream, cocoa powder, almond milk, agave

Fruit Fiesta
Oats, mixed berries, banana, dates ,soy milk, dairy free ice cream

Immune boosters
Regular 16 oz £6
Smoothie Bowl £5.50 * Available on a seasonal basis

The yellow one: Pineapple turmeric
Pineapple, banana, lemon, agave, ginger,tumeric,coconut water

The Red one : Citrus Berry Ginger
Orange, strawberry, lemon, ginger , almond milk

The Orange one : Citrus carrot
Grapefruit, clementine, carrot,mango,yogurt,lemon,tumeric

Teas
Regular £2
Jade lotus
Breakfast blend
Lemon & ginger
Moroccan mint

Iced Frappucino
* Substitute for non dairy for .50p
Regular £3.50
Cappuccino - expresso, milk, ice
Mocha- cocoa ,milk, ice
Strawberry's n cream- Strawberry,cream,ice
Zesty Sencha - Matcha, cream, ice
Vanilla Bean- Vanilla, cream, ice
Blend Sandwiches
£4.50

Avocado
Avocado , mozerella,tomatoe, pesto

Spicy Tuna
Tuna, Chilli peppers, mayo, salt, pepper

Fishavo
Tuna, avocado, mayo, salt, pepper

BLT
Turkey Rasher, lettuce, mayo, tomatoe

American Grilled Cheese
Mature Cheddar , wholewheat bread
*sourdough bread is optional

Yogurt
£3
Coconut ,Vanilla yogurt , banana, granola

Bowls
£4.50
+ protein=.50p

Acai Bowl
Acai, Raspberry,blueberry,banana,almond milk, granola
*Topping: granola and ½ banana sliced ,chia seeds

Cocoa Bowl
Cocoa,banana,peanut butter,almond milk
Toppings : chocolate granola, peanut butter ,chia seeds,1/2 banana sliced

Target Market(s)

any age , predominately ages 20+

Industry/Entity Type

food & drink

Colors

Designer to choose colors to be used in the design.

Requirements
Must have
• clean, modern concept
Nice to have
• white background, fruits in the background -animated or actual ones
Should not have
• no dark background concepts

```html
<!DOCTYPE html>
<html lang="en">
<head>
<meta charset="utf-8">
<title>Fresh Juice / Blends Menu</title>
<link href="https://fonts.googleapis.com/css2?family=Montserrat:wght@500;600;700;800&family=Raleway:wght@400;500&display=swap" rel="stylesheet">
<style>
:root{
  --pink:#e5459a;
  --pink-soft:#ef7ab8;
  --yellow:#fdcc2b;
  --green:#2e620b;
  --sky:#d8edf9;
  --sky-ink:#2aa8e0;
  --ink:#3a3a3a;
  --white:#ffffff;
}
*{margin:0;padding:0;box-sizing:border-box}
html,body{width:686px;height:1200px;overflow:hidden;background:var(--white)}
body{position:relative;font-family:"Raleway",sans-serif;color:var(--ink)}
.abs{position:absolute}

.main-title{left:23px;top:14px;font:800 37px/1 "Montserrat",sans-serif;color:var(--pink);letter-spacing:0.5px}
.main-sub{left:474px;top:22px;font:700 13px/14px "Montserrat",sans-serif;color:var(--pink)}
.create{left:25px;top:65px;font:700 10px/1 "Montserrat",sans-serif;color:var(--pink);letter-spacing:8.6px}
.size-pill{top:63px;height:16px;width:113px;border:1px solid var(--pink);border-radius:8px;display:flex;align-items:center;overflow:hidden;font:700 10px/1 "Montserrat",sans-serif}
.size-pill .lbl{background:var(--pink);color:var(--white);height:100%;display:flex;align-items:center;padding:0 7px;width:67px;border-radius:0 8px 8px 0}
.size-pill .val{color:var(--pink);flex:1;text-align:center}

.band-base{left:24px;top:95px;width:157px;height:43px;background:var(--yellow)}
.band-add{left:181px;top:95px;width:482px;height:43px}
.band-label{color:var(--pink);font-family:"Montserrat",sans-serif;font-weight:800}
.base-label{left:40px;top:103px;font-size:12px;line-height:12.5px}
.add-label{left:201px;top:111px;font-size:12.5px}

.base-panel{left:24px;top:138px;width:157px;height:206px;box-shadow:2px 3px 6px rgba(0,0,0,0.08)}
.chip{position:absolute;height:29px;width:134px;background:var(--yellow);border-radius:10px;display:flex;align-items:center;overflow:hidden}
.chip .pic{width:30px;height:100%;border-radius:14px 0 0 14px;flex:none}
.chip .name{font:700 10px/1 "Montserrat",sans-serif;color:var(--pink);padding-left:5px;white-space:nowrap}
.ingr .chip{width:108px}
.ingr .chip.wide{width:119px}

.recipe .title{font:700 20px/20px "Montserrat",sans-serif;color:var(--yellow);white-space:nowrap}
.recipe p{font-size:10.3px;line-height:12.3px;margin-top:1px;text-transform:uppercase;color:#444}
.kj{position:absolute;width:105px;height:16px;border:1px solid var(--yellow);border-radius:8px;display:flex;align-items:center;overflow:hidden;font:500 11px/1 "Montserrat",sans-serif}
.kj .lbl{background:var(--yellow);color:var(--white);height:100%;width:62px;display:flex;align-items:center;padding-left:6px;border-radius:0 8px 8px 0}
.kj .val{color:var(--yellow);font-weight:700;flex:1;text-align:center;font-size:10px}

.banner{position:absolute;height:71px;top:449px;display:flex;align-items:center;padding-left:22px;gap:8px}
.banner.protein{left:23px;width:308px;background:var(--pink);border-radius:0 36px 36px 0}
.banner.vegan{left:345px;width:307px;background:var(--green);border-radius:0 36px 36px 0}
.banner .big{font:800 34px/1 "Montserrat",sans-serif;color:var(--yellow)}
.banner .tag{font:500 12px/14px "Montserrat",sans-serif;color:var(--white)}
.notch{position:absolute;top:471px;width:0;height:0;border-top:14px solid transparent;border-bottom:14px solid transparent;border-left:11px solid #d8d8d8}

.col-panel{top:520px;height:520px;box-shadow:2px 4px 8px rgba(0,0,0,0.07)}

.item{position:absolute;padding-left:8px}
.item .title{font:700 20.5px/23px "Montserrat",sans-serif;white-space:nowrap}
.item p{font-size:10.1px;line-height:12.4px;text-transform:uppercase;color:#555;margin-top:0}
.item p small{font-size:7px}
.protein-item{left:51px;border-left:1.5px solid var(--pink-soft);width:266px}
.protein-item .title{color:var(--pink)}
.vegan-item{left:372px;border-left:2px solid var(--green);width:280px}
.vegan-item .title{color:var(--green)}

.prow{position:absolute;display:flex;gap:7px}
.pp{height:14px;border-radius:7px;display:flex;align-items:center;justify-content:space-between;font:500 8.5px/1 "Montserrat",sans-serif;color:var(--white);padding:0 4px}
.pp .k{background:var(--white);border-radius:7px;height:12px;display:flex;align-items:center;justify-content:center;font-size:7.5px}
.pp .p{font-weight:600}
.pp-pink{background:var(--pink-soft);width:130px}
.pp-pink .k{color:var(--pink);width:48px}
.pp-green{background:var(--green)}
.pp-green .k{color:var(--green);width:38px}
.pp-orig{width:94px}
.pp-sm{width:86px}

.intake{left:26px;top:1077px;font:700 11.8px/1 "Montserrat",sans-serif;color:#444}
.fine{left:26px;top:1097px;width:288px;font:400 5.3px/6.2px "Raleway",sans-serif;color:#555;text-transform:uppercase}

.extra-box{top:1136px;height:58px;background:var(--sky);border-radius:6px;text-align:center;padding-top:5px}
.extra-box .head{font:800 15px/1 "Montserrat",sans-serif;color:var(--sky-ink)}
.extra-box ul{list-style:none;font:600 6.8px/9.8px "Montserrat",sans-serif;color:#444;margin-top:3px}
.booster-grid{display:grid;grid-template-columns:96px 60px;justify-content:center;font:600 6.8px/9.8px "Montserrat",sans-serif;color:#444;margin-top:3px;white-space:nowrap}
</style>
</head>
<body>

<header>
  <h1 class="abs main-title">FRESH JUICE/BLENDS</h1>
  <div class="abs main-sub">FRESHLY SQUEEZED OR<br>WHOLE FRUIT BLENDED</div>
  <div class="abs create">CREATE YOUR OWN</div>
  <div class="abs size-pill" style="left:299px"><span class="lbl">ORIGINAL</span><span class="val">8.00</span></div>
  <div class="abs size-pill" style="left:417px"><span class="lbl">MEDIUM</span><span class="val">8.00</span></div>
  <div class="abs size-pill" style="left:534px"><span class="lbl">JUNIOR</span><span class="val">8.00</span></div>
</header>

<section class="builder">
  <div class="abs base-panel"></div>
  <div class="abs band-base"></div>
  <svg class="abs band-add" viewBox="0 0 482 43" width="482" height="43" aria-hidden="true">
    <polygon points="0,0 462,0 482,21.5 462,43 0,43 6,21.5" fill="#fdcc2b"/>
  </svg>
  <svg class="abs" style="left:24px;top:104px" width="8" height="24" aria-hidden="true"><polygon points="0,0 8,12 0,24" fill="#e8e8e8"/></svg>
  <div class="abs band-label base-label">CHOOSE<br>YOUR BASE</div>
  <div class="abs band-label add-label">ADD YOUR INGREDIENTS</div>

  <div class="base">
    <div class="chip" style="left:32px;top:148px"><span class="pic" role="img" aria-label="Photo of red apples" style="background:radial-gradient(circle at 40% 40%,#e0443a,#8e1018)"></span><span class="name">APPLE</span></div>
    <div class="chip" style="left:32px;top:181px"><span class="pic" role="img" aria-label="Photo of carrots" style="background:linear-gradient(135deg,#f59a38,#e0621a)"></span><span class="name">CARROTS</span></div>
    <div class="chip" style="left:32px;top:214px"><span class="pic" role="img" aria-label="Photo of oranges with leaves" style="background:linear-gradient(135deg,#5f8a3a,#e89a30)"></span><span class="name">ORANGE</span></div>
    <div class="chip" style="left:32px;top:247px"><span class="pic" role="img" aria-label="Photo of pineapple pieces" style="background:linear-gradient(135deg,#f6d35a,#d9a21e)"></span><span class="name">PINEAPPLE</span></div>
    <div class="chip" style="left:32px;top:280px"><span class="pic" role="img" aria-label="Photo of young coconuts" style="background:linear-gradient(135deg,#b7c78a,#6f8a4a)"></span><span class="name">COCONUT WATER</span></div>
    <div class="chip" style="left:32px;top:313px"><span class="pic" role="img" aria-label="Photo of watermelon slices" style="background:linear-gradient(135deg,#e24a52,#3f7a2a)"></span><span class="name">WATERMELON</span></div>
  </div>

  <div class="ingr">
    <div class="chip" style="left:189px;top:148px"><span class="pic" role="img" aria-label="Photo of banana slices" style="background:#ece0c2"></span><span class="name">BANANA</span></div>
    <div class="chip" style="left:189px;top:181px"><span class="pic" role="img" aria-label="Photo of beetroot" style="background:#a3122a"></span><span class="name">BEETROOT</span></div>
    <div class="chip" style="left:189px;top:214px"><span class="pic" role="img" aria-label="Photo of blueberries" style="background:#3b5aa0"></span><span class="name">BLUEBERRY</span></div>
    <div class="chip" style="left:189px;top:247px"><span class="pic" role="img" aria-label="Photo of celery" style="background:#5e9232"></span><span class="name">CELERY</span></div>

    <div class="chip" style="left:304px;top:148px"><span class="pic" role="img" aria-label="Photo of cucumbers" style="background:#3f8a22"></span><span class="name">CUCUMBER</span></div>
    <div class="chip" style="left:304px;top:181px"><span class="pic" role="img" aria-label="Photo of dates" style="background:#5a2a18"></span><span class="name">DATES</span></div>
    <div class="chip" style="left:304px;top:214px"><span class="pic" role="img" aria-label="Photo of ginger root" style="background:#d5c07c"></span><span class="name">GINGER</span></div>
    <div class="chip" style="left:304px;top:247px"><span class="pic" role="img" aria-label="Photo of red grapes" style="background:#7a1f3a"></span><span class="name">GRAPES</span></div>

    <div class="chip" style="left:418px;top:149px"><span class="pic" role="img" aria-label="Photo of kale" style="background:#3f6b22"></span><span class="name">KALE</span></div>
    <div class="chip" style="left:418px;top:182px"><span class="pic" role="img" aria-label="Photo of lemon slices" style="background:#f0df78"></span><span class="name">LEMON</span></div>
    <div class="chip" style="left:418px;top:215px"><span class="pic" role="img" aria-label="Photo of mangoes" style="background:#e9a93a"></span><span class="name">MANGO</span></div>
    <div class="chip" style="left:418px;top:249px"><span class="pic" role="img" aria-label="Photo of mint leaves" style="background:#5fa83a"></span><span class="name">MINT</span></div>

    <div class="chip wide" style="left:533px;top:151px"><span class="pic" role="img" aria-label="Photo of passion fruit" style="background:#6b3a5a"></span><span class="name">PASSION FRUIT</span></div>
    <div class="chip wide" style="left:533px;top:184px"><span class="pic" role="img" aria-label="Photo of raspberries" style="background:#c0344a"></span><span class="name">RASPBERRY</span></div>
    <div class="chip wide" style="left:533px;top:216px"><span class="pic" role="img" aria-label="Photo of spinach leaves" style="background:#3f8a2a"></span><span class="name">SPINACH</span></div>
    <div class="chip wide" style="left:533px;top:249px"><span class="pic" role="img" aria-label="Photo of strawberries" style="background:#d0202a"></span><span class="name">STRAWBERRY</span></div>
  </div>

  <div class="abs recipe" style="left:195px;top:294px;width:140px">
    <div class="title">IMMUNITY</div>
    <p>Watermelon, orange, strawberries, and ice + immunity booster</p>
  </div>
  <div class="abs recipe" style="left:345px;top:294px;width:160px">
    <div class="title">GARDEN GLOW</div>
    <p>Orange, apple, carrot, cucumber, celery, spinach, beetroot, and ice + vita booster</p>
  </div>
  <div class="abs recipe" style="left:512px;top:294px;width:150px">
    <div class="title">MINT<br>BREEZE</div>
    <p>Mint, apple, spinach, cucumber, celery, and ice</p>
  </div>

  <div class="kj" style="left:195px;top:368px"><span class="lbl">ORIGINAL</span><span class="val">621 KJ</span></div>
  <div class="kj" style="left:195px;top:387px"><span class="lbl">MEDIUM</span><span class="val">477 KJ</span></div>
  <div class="kj" style="left:195px;top:406px"><span class="lbl">JUNIOR</span><span class="val">260 KJ</span></div>
  <div class="kj" style="left:345px;top:368px"><span class="lbl">ORIGINAL</span><span class="val">621 KJ</span></div>
  <div class="kj" style="left:345px;top:387px"><span class="lbl">MEDIUM</span><span class="val">477 KJ</span></div>
  <div class="kj" style="left:345px;top:406px"><span class="lbl">JUNIOR</span><span class="val">260 KJ</span></div>
  <div class="kj" style="left:512px;top:368px"><span class="lbl">ORIGINAL</span><span class="val">621 KJ</span></div>
  <div class="kj" style="left:512px;top:387px"><span class="lbl">MEDIUM</span><span class="val">477 KJ</span></div>
  <div class="kj" style="left:512px;top:406px"><span class="lbl">JUNIOR</span><span class="val">260 KJ</span></div>
</section>

<section class="protein-col">
  <div class="abs col-panel" style="left:23px;width:322px"></div>
  <div class="banner protein"><span class="big">PROTEIN</span><span class="tag">SOURCE OF<br>PROTEIN</span></div>
  <span class="notch" style="left:23px"></span>

  <div class="item protein-item" style="top:536px">
    <div class="title">LIFT OFF</div>
    <p>Strawberries, banana, low fat milk, strawberry yoghurt, vanilla, yoghurt, whey protein, and ice (20.5<small>G</small> of protein)</p>
  </div>
  <div class="prow" style="left:53px;top:606px"><div class="pp pp-pink">ORIGINAL<span class="k">1630 KJ</span><span class="p">8.00</span></div><div class="pp pp-pink">MEDIUM<span class="k">1170 KJ</span><span class="p">7.50</span></div></div>

  <div class="item protein-item" style="top:637px">
    <div class="title">SUNRISE SURGE</div>
    <p>Mango, banana, tropical juice, mango yoghurt, and ice + superfruit (8.3<small>G</small> of protein)</p>
  </div>
  <div class="prow" style="left:55px;top:698px"><div class="pp pp-pink">ORIGINAL<span class="k">1730 KJ</span><span class="p">8.00</span></div><div class="pp pp-pink">MEDIUM<span class="k">1350 KJ</span><span class="p">7.50</span></div></div>

  <div class="item protein-item" style="top:729px">
    <div class="title">MELON MARVEL</div>
    <p>Strawberries, freshly juiced watermelon, strawberry yoghurt, whey protein, and ice + superfruit booster (13.1<small>G</small> of protein)</p>
  </div>
  <div class="prow" style="left:55px;top:802px"><div class="pp pp-pink">ORIGINAL<span class="k">798 KJ</span><span class="p">8.00</span></div><div class="pp pp-pink">MEDIUM<span class="k">651 KJ</span><span class="p">7.50</span></div></div>

  <div class="item protein-item" style="top:834px">
    <div class="title">PROTEIN PRIME</div>
    <p>Banana, muesli, dates, honey, coconut water, coconut mylk, vanilla yoghurt, whey protein, and ice + immunity and vita booster (30.1<small>G</small> of protein)</p>
  </div>
  <div class="prow" style="left:53px;top:917px"><div class="pp pp-pink">ORIGINAL<span class="k">2320 KJ</span><span class="p">9.20</span></div><div class="pp pp-pink">MEDIUM<span class="k">1490 KJ</span><span class="p">8.70</span></div></div>

  <div class="item protein-item" style="top:957px">
    <div class="title">CHOC POWER PUSH</div>
    <p>Chocolate powder, banana, oats, chia seeds, coconut water, coconut mylk, vanilla yoghurt, whey protein, and ice (24.2<small>G</small> of protein)</p>
  </div>
  <div class="prow" style="left:53px;top:1043px"><div class="pp pp-pink">ORIGINAL<span class="k">2330 KJ</span><span class="p">9.20</span></div><div class="pp pp-pink">MEDIUM<span class="k">1760 KJ</span><span class="p">8.70</span></div></div>
</section>

<section class="vegan-col">
  <div class="abs col-panel" style="left:345px;width:307px"></div>
  <div class="banner vegan"><span class="big">VEGAN</span><span class="tag">PLANT BASED AND<br>LOW GLUTEN</span></div>
  <span class="notch" style="left:345px"></span>

  <div class="item vegan-item" style="top:536px">
    <div class="title">MANGO PASH DASH</div>
    <p>Mango, passionfruit, banana, mango nectar, frozen coconut cream, and ice</p>
  </div>
  <div class="prow" style="left:367px;top:599px;gap:4px"><div class="pp pp-green pp-orig">ORIG<span class="k">2330 KJ</span><span class="p">8.00</span></div><div class="pp pp-green pp-sm">MED<span class="k">1850 KJ</span><span class="p">7.50</span></div><div class="pp pp-green pp-sm">JNR<span class="k">1360 KJ</span><span class="p">6.50</span></div></div>

  <div class="item vegan-item" style="top:630px">
    <div class="title">LYCHEE BERRY BLISS</div>
    <p>Lychees, rasperries, mango, mango nectar, frozen coconut cream, and ice</p>
  </div>
  <div class="prow" style="left:367px;top:692px;gap:4px"><div class="pp pp-green pp-orig">ORIG<span class="k">1750 KJ</span><span class="p">8.00</span></div><div class="pp pp-green pp-sm">MED<span class="k">1440 KJ</span><span class="p">7.50</span></div><div class="pp pp-green pp-sm">JNR<span class="k">1200 KJ</span><span class="p">6.50</span></div></div>

  <div class="item vegan-item" style="top:722px">
    <div class="title">COCO CHOC CRUSH</div>
    <p>Chocolate powder, banana, soy mylk, coconut mylk, frozen coconut cream, and ice</p>
  </div>
  <div class="prow" style="left:367px;top:780px;gap:4px"><div class="pp pp-green pp-orig">ORIG<span class="k">2420 KJ</span><span class="p">8.00</span></div><div class="pp pp-green pp-sm">MED<span class="k">1900 KJ</span><span class="p">7.50</span></div><div class="pp pp-green pp-sm">JNR<span class="k">1400 KJ</span><span class="p">6.50</span></div></div>

  <div class="item vegan-item" style="top:809px">
    <div class="title">ISLAND GREEN</div>
    <p>Mango, passionfruit, banana, spinach, mango nectar, coconut mylk, coconut water, and ice</p>
  </div>
  <div class="prow" style="left:367px;top:866px;gap:4px"><div class="pp pp-green pp-orig">ORIG<span class="k">1160 KJ</span><span class="p">8.00</span></div><div class="pp pp-green pp-sm">MED<span class="k">887 KJ</span><span class="p">7.50</span></div><div class="pp pp-green pp-sm">JNR<span class="k">664 KJ</span><span class="p">6.50</span></div></div>

  <div class="item vegan-item" style="top:891px">
    <div class="title">GREEN GARDEN SUPER<br>SMOOTHIE</div>
    <p>Apple, pineapple, grapes, kale, spinach, cucumber, lemon, banana, mint, coconut water, and ice + all greens booster</p>
  </div>
  <div class="prow" style="left:367px;top:991px;gap:4px"><div class="pp pp-green pp-orig">ORIG<span class="k">726 KJ</span><span class="p">9.20</span></div><div class="pp pp-green pp-sm">MED<span class="k">505 KJ</span><span class="p">8.70</span></div><div class="pp pp-green pp-sm">JNR<span class="k">361 KJ</span><span class="p">7.70</span></div></div>

  <div class="item vegan-item" style="top:1025px">
    <div class="title">PLANT POWER PUNCH</div>
    <p>Mango, passionfruit, banana, grapes, spinach, pineapple, dates, coconut water, coconut mylk, plant based proteins, and ice + all green booster (11.1<small>G</small> of protein)</p>
  </div>
  <div class="prow" style="left:367px;top:1107px;gap:4px"><div class="pp pp-green pp-orig">ORIG<span class="k">1230 KJ</span><span class="p">9.20</span></div><div class="pp pp-green pp-sm">MED<span class="k">910 KJ</span><span class="p">8.70</span></div><div class="pp pp-green pp-sm">JNR<span class="k">669 KJ</span><span class="p">7.70</span></div></div>
</section>

<footer>
  <div class="abs intake">THE AVERAGE ADULT DAILY INTAKE IS 8700 kJ</div>
  <p class="abs fine">The chocolate powder, banana, oats, chia seeds, coconut water, coconut mylk vanilla yoghurt, whey protein, and ice (24.2g of protein). The chocolate powder, banana, oats, chia seeds, coconut water, coconut mylk, vanilla yoghurt, whey protein, and ice (24.2g of protein). The chocolate powder, banana, oats, chia seeds, coconut water, coconut mylk vanilla yoghurt, whey protein, and ice (24.2g of protein). The chocolate powder, banana, oats, chia seeds, coconut water, coconut mylk, vanilla yoghurt, whey protein, and ice (24.2g of protein). The chocolate powder, banana, oats, chia seeds, coconut water, coconut mylk vanilla yoghurt, whey protein, and ice (24.2g of protein). The chocolate powder, banana, oats, chia seeds, coconut water, coconut mylk, vanilla yoghurt, whey protein, and ice (24.2g of protein).</p>

  <div class="abs extra-box" style="left:324px;width:95px">
    <div class="head">EXTRAS</div>
    <ul><li>FRUIT &amp; VEG</li><li>CHIA SEEDS</li><li>COCONUT WATER</li></ul>
  </div>
  <div class="abs extra-box" style="left:424px;width:75px">
    <div class="head">MYLK</div>
    <ul><li>SOY MYLK</li><li>ALMOND MYLK</li></ul>
  </div>
  <div class="abs extra-box" style="left:504px;width:163px">
    <div class="head">BOOSTER</div>
    <div class="booster-grid"><span>PROTEIN/PLANT BASED</span><span>VITA</span><span>IMMUNITY</span><span>ALL GREENS</span><span>ENERGISER</span><span>SUPERFRIEND</span></div>
  </div>
</footer>

</body>
</html>
```